Adwords Banner for unique handmade Jewelery

We need one Banner for our Jewelerys
in 4 sizes:
300x250px
336x280px
728x90px
160x600px

http://www.torvik-mela.de/schmuck/2/

```html
<!DOCTYPE html>
<html lang="de">
<head>
<meta charset="utf-8">
<title>torvik &amp; mela – Banner Set</title>
<link rel="stylesheet" href="https://fonts.googleapis.com/css2?family=Cormorant+Garamond:ital,wght@0,500;1,500&display=swap">
<style>
  :root {
    --page: #ffffff;
    --board: #f2e1d6;
    --board-edge: #ead4c6;
    --ink-dark: #0c0c0c;
    --ink-mid: #262626;
    --pink: #c8608e;
    --name-light: #e9e4e6;
    --name-dark: #6b6466;
    --teal: #47c3cc;
    --teal-soft: #a6e2e6;
    --rose: #f07aa2;
    --silver: #c9cbcd;
    --white: #ffffff;
  }
  * { margin: 0; padding: 0; box-sizing: border-box; }
  html, body { width: 1200px; height: 1200px; overflow: hidden; background: var(--page); }
  .canvas { position: relative; width: 1200px; height: 1200px; background: var(--page); }
  .board {
    position: absolute; left: 70px; top: 70px; width: 1060px; height: 1060px;
    background: linear-gradient(160deg, var(--board) 0%, var(--board-edge) 100%);
  }
  .brand-name {
    position: absolute;
    font-family: "Cormorant Garamond", Georgia, serif;
    font-weight: 500; font-style: normal; white-space: nowrap; letter-spacing: 0.5px; line-height: 1;
  }
  .brand-name::before {
    content: ""; display: inline-block; width: 0.32em; height: 0.32em;
    border-radius: 50%; background: var(--pink); margin-right: 0.22em; vertical-align: middle;
  }
  .board-brand { left: 4px; top: 14px; font-size: 50px; color: var(--name-dark); }
  .hero-photo {
    position: absolute; left: 0; top: 78px; width: 420px; height: 318px;
    background:
      radial-gradient(ellipse 90px 110px at 40px 180px, var(--teal) 0%, var(--teal-soft) 55%, transparent 75%),
      radial-gradient(ellipse 80px 75px at 220px 135px, var(--rose) 0%, #f6b1c7 55%, transparent 78%);
  }
  .banner {
    position: absolute; overflow: hidden;
    background: linear-gradient(180deg, var(--ink-mid) 0%, var(--ink-dark) 60%, #050505 100%);
    box-shadow: 0 1px 4px rgba(0,0,0,0.25);
  }
  .banner .brand-name { color: var(--name-light); }
  .banner-medium { left: 414px; top: 153px; width: 322px; height: 269px; }
  .banner-sky { left: 748px; top: 153px; width: 173px; height: 646px; }
  .banner-large { left: 374px; top: 498px; width: 362px; height: 301px; }
  .banner-leader { left: 138px; top: 810px; width: 783px; height: 96px; }
  .banner-medium .brand-name { left: 24px; top: 20px; font-size: 34px; }
  .banner-sky .brand-name { left: 6px; top: 10px; font-size: 19px; }
  .banner-large .brand-name { left: 14px; top: 16px; font-size: 38px; }
  .banner-leader .brand-name { left: 8px; top: 28px; font-size: 36px; }
  .product-photo { position: absolute; }
  .medium-photo {
    left: 110px; top: 70px; width: 210px; height: 150px;
    background:
      radial-gradient(ellipse 42px 38px at 95px 100px, var(--teal) 0%, var(--teal-soft) 55%, transparent 78%),
      radial-gradient(ellipse 30px 28px at 160px 105px, var(--rose) 0%, #f6b1c7 55%, transparent 80%);
  }
  .sky-photo {
    left: 0; top: 40px; width: 173px; height: 420px;
    background:
      radial-gradient(ellipse 50px 46px at 75px 110px, var(--rose) 0%, #f6b1c7 55%, transparent 80%),
      radial-gradient(ellipse 70px 20px at 85px 230px, var(--teal) 0%, rgba(71,195,204,0.4) 60%, transparent 85%),
      radial-gradient(ellipse 65px 55px at 75px 360px, var(--teal) 0%, var(--silver) 60%, transparent 82%);
  }
  .large-photo {
    left: 60px; top: 70px; width: 240px; height: 150px;
    background: radial-gradient(ellipse 95px 70px at 120px 75px, var(--teal) 0%, var(--teal-soft) 45%, var(--silver) 65%, transparent 82%);
  }
  .leader-photo {
    left: 230px; top: 0; width: 390px; height: 96px;
    background:
      radial-gradient(ellipse 60px 48px at 70px 48px, var(--teal) 0%, var(--teal-soft) 55%, transparent 80%),
      radial-gradient(ellipse 50px 40px at 200px 48px, var(--silver) 0%, rgba(201,203,205,0.4) 60%, transparent 85%),
      radial-gradient(ellipse 60px 48px at 320px 48px, var(--teal) 0%, var(--teal-soft) 55%, transparent 80%);
  }
  .pink-band { position: absolute; left: 0; bottom: 0; width: 100%; }
  .leader-arrow { position: absolute; left: 620px; top: 0; }
  .tag-line, .tag-sub {
    position: absolute; font-family: "Cormorant Garamond", Georgia, serif;
    font-style: italic; font-weight: 500; color: var(--white); white-space: nowrap;
  }
  .tag-line .lead { font-size: 0.55em; }
  .banner-medium .tag-line { left: 12px; top: 202px; font-size: 28px; line-height: 32px; }
  .banner-medium .tag-sub { left: 45px; top: 235px; font-size: 22px; line-height: 24px; }
  .banner-large .tag-line { left: 58px; top: 236px; font-size: 38px; line-height: 40px; }
  .banner-large .tag-sub { left: 190px; top: 276px; font-size: 18px; line-height: 20px; }
  .banner-sky .tag-line { left: 16px; top: 574px; font-size: 34px; line-height: 38px; }
  .banner-sky .tag-sub { left: 40px; top: 612px; font-size: 19px; line-height: 20px; }
  .banner-leader .tag-line { left: 634px; top: 18px; font-size: 32px; line-height: 36px; }
  .banner-leader .tag-sub { left: 678px; top: 56px; font-size: 18px; line-height: 20px; }
</style>
</head>
<body>
<div class="canvas">
  <div class="board">
    <span class="brand-name board-brand">torvik &amp; mela</span>
    <div class="hero-photo" role="img" aria-label="Close-up of a silver chain necklace with a turquoise and a pink glass heart bead"></div>

    <section class="banner banner-medium" aria-label="Banner 300 x 250">
      <span class="brand-name">torvik &amp; mela</span>
      <div class="product-photo medium-photo" role="img" aria-label="Silver chain with turquoise and pink glass heart beads"></div>
      <p class="tag-line"><span class="lead">The </span>Riches</p>
      <p class="tag-sub">Collection</p>
    </section>

    <section class="banner banner-sky" aria-label="Banner 160 x 600">
      <span class="brand-name">torvik &amp; mela</span>
      <div class="product-photo sky-photo" role="img" aria-label="Pink glass heart on a chain, turquoise bead bracelet and turquoise glass ring"></div>
      <svg class="pink-band" width="173" height="92" viewBox="0 0 173 92" aria-hidden="true">
        <path d="M0 28 Q86 -6 173 28 L173 92 L0 92 Z" fill="var(--pink)"/>
      </svg>
      <p class="tag-line"><span class="lead">The </span>Perfect</p>
      <p class="tag-sub">Collection</p>
    </section>

    <section class="banner banner-large" aria-label="Banner 336 x 280">
      <span class="brand-name">torvik &amp; mela</span>
      <div class="product-photo large-photo" role="img" aria-label="Silver ring with a large turquoise glass stone"></div>
      <svg class="pink-band" width="362" height="84" viewBox="0 0 362 84" aria-hidden="true">
        <path d="M0 30 Q181 -8 362 30 L362 84 L0 84 Z" fill="var(--pink)"/>
      </svg>
      <p class="tag-line"><span class="lead">The </span>Perfect Fit</p>
      <p class="tag-sub">Collection</p>
    </section>

    <section class="banner banner-leader" aria-label="Banner 728 x 90">
      <span class="brand-name">torvik &amp; mela</span>
      <div class="product-photo leader-photo" role="img" aria-label="Turquoise glass beads with silver spacers"></div>
      <svg class="leader-arrow" width="163" height="96" viewBox="0 0 163 96" aria-hidden="true">
        <path d="M28 0 L163 0 L163 96 L28 96 L0 48 Z" fill="var(--pink)"/>
      </svg>
      <p class="tag-line"><span class="lead">The </span>Perfect</p>
      <p class="tag-sub">Collection</p>
    </section>
  </div>
</div>
</body>
</html>
```